Best in class business looking for best in class stationery that accurately reflects the brand image we are trying to build as the brand expands throughout the country. The Varying items should be an eye catching design that makes even the simplest letter or small business card stand out in the crowd.

Target Market(s)

Professionals

Industry/Entity Type

Real Estate

Other font styles liked:
• See atttached logo

Requirements
Must have
• Letterhead
• Business cards
• Envelopes
• Labels for larger mailings
Nice to have
• Folders
• Notebook
Should not have
• Stale design elements

```html
<!DOCTYPE html>
<html lang="en">
<head>
<meta charset="utf-8">
<title>Ridgeline Property Group – Stationery</title>
<link rel="stylesheet" href="https://fonts.googleapis.com/css2?family=Open+Sans:ital,wght@0,400;0,600;0,700;1,400&display=swap">
<style>
  :root {
    --navy: #1f2c86;
    --blue: #2b3d9e;
    --mid: #3a56b8;
    --soft: #e9ebf4;
    --paper: #ffffff;
    --sand: #e6d5b3;
    --mist: #e4e8ea;
    --night: #121212;
    --stone: #d9dadb;
    --ink: #1f2c86;
  }
  * { box-sizing: border-box; margin: 0; padding: 0; }
  html, body { width: 1200px; height: 2571px; overflow: hidden; }
  body { position: relative; font-family: "Open Sans", Arial, sans-serif; color: var(--ink); background: var(--paper); }

  .section { position: absolute; left: 0; width: 1200px; overflow: hidden; }
  .suite { top: 0; height: 789px; background: linear-gradient(118deg, var(--sand) 0 47%, var(--mist) 47% 100%); }
  .cards-showcase { top: 789px; height: 866px; background: radial-gradient(ellipse at center, #2a2a2a 0%, var(--night) 70%); }
  .mailing { top: 1655px; height: 916px; background: var(--paper); }
  .mailing .backdrop { position: absolute; left: 540px; top: 0; width: 660px; height: 916px; background: var(--stone); }

  .item { position: absolute; box-shadow: 0 6px 18px rgba(0,0,0,.22); }
  .paper { background: var(--paper); }
  .deep { background: linear-gradient(150deg, var(--mid), var(--navy)); color: #fff; }

  .wordmark { display: flex; align-items: center; gap: 6px; font-weight: 700; letter-spacing: .06em; text-transform: uppercase; white-space: nowrap; }
  .wordmark .mark { display: inline-block; background: currentColor; flex: none; }
  .wordmark.center { justify-content: center; }

  /* envelope */
  .envelope { left: 60px; top: 50px; width: 480px; height: 220px; }
  .envelope .flap { position: absolute; left: 0; top: 0; width: 100%; height: 46px; background: linear-gradient(90deg, var(--navy), var(--mid)); }

  /* small cards */
  .mini-back { left: 60px; top: 315px; width: 200px; height: 114px; }
  .mini-back .wordmark { position: absolute; left: 0; right: 0; top: 48px; font-size: 9px; }
  .mini-front { left: 285px; top: 315px; width: 200px; height: 114px; }
  .mini-front .wordmark { position: absolute; right: 10px; top: 14px; font-size: 6.5px; color: var(--navy); }
  .mini-front .details { position: absolute; left: 12px; top: 16px; font-size: 6px; line-height: 1.5; color: var(--navy); }
  .mini-front .details b { font-size: 8px; }
  .mini-front .band { position: absolute; left: 0; bottom: 0; width: 100%; height: 8px; background: var(--blue); }

  /* label */
  .label-sheet { left: 60px; top: 470px; width: 480px; height: 265px; }
  .label-sheet .wordmark { position: absolute; left: 26px; top: 30px; font-size: 12px; color: var(--navy); }
  .label-sheet .return { position: absolute; left: 26px; top: 150px; font-size: 9px; line-height: 1.5; color: var(--navy); }
  .band-split { position: absolute; left: 0; bottom: 0; width: 100%; height: 16px; display: flex; }
  .band-split span:nth-child(1) { flex: 0 0 30%; background: var(--navy); }
  .band-split span:nth-child(2) { flex: 0 0 30%; background: var(--mid); }
  .band-split span:nth-child(3) { flex: 1; background: var(--navy); }

  /* folder */
  .folder { left: 585px; top: 200px; width: 280px; height: 396px; }
  .folder .wordmark { position: absolute; right: 22px; top: 60px; font-size: 10px; }
  .folder .stripe { position: absolute; left: 0; bottom: 0; width: 100%; height: 120px; background: linear-gradient(180deg, rgba(255,255,255,0), rgba(255,255,255,.08)); }

  /* letterhead */
  .letterhead { left: 885px; top: 110px; width: 280px; height: 396px; }
  .letterhead .wordmark { position: absolute; right: 20px; top: 26px; font-size: 9px; color: var(--navy); }
  .letterhead .rule { position: absolute; left: 20px; right: 20px; bottom: 34px; height: 1px; background: var(--navy); opacity: .5; }
  .letterhead .footer { position: absolute; left: 20px; right: 20px; bottom: 20px; font-size: 5.5px; color: var(--navy); display: flex; justify-content: space-between; }
  .letterhead .edge { position: absolute; left: 0; bottom: 0; width: 100%; height: 7px; background: var(--navy); }
  .letterhead .edge-top { position: absolute; left: 0; top: 0; width: 100%; height: 4px; background: var(--navy); }

  /* showcase cards */
  .card-back { left: 90px; top: 300px; width: 490px; height: 280px; }
  .card-back .wordmark { position: absolute; left: 0; right: 0; top: 122px; font-size: 22px; }
  .card-back .sub-rule { position: absolute; left: 120px; right: 120px; top: 162px; height: 1px; background: rgba(255,255,255,.6); }
  .card-front { left: 620px; top: 300px; width: 490px; height: 280px; }
  .card-front .wordmark { position: absolute; right: 26px; top: 40px; font-size: 14px; color: var(--navy); }
  .card-front .name { position: absolute; left: 30px; top: 54px; font-size: 21px; font-weight: 700; font-style: italic; color: var(--navy); }
  .card-front .role { position: absolute; left: 30px; top: 84px; font-size: 12px; font-style: italic; color: var(--navy); }
  .contact { position: absolute; left: 30px; top: 114px; list-style: none; font-size: 12.5px; line-height: 1.42; color: var(--navy); }
  .contact li { display: flex; align-items: flex-start; gap: 8px; }
  .contact svg { flex: none; margin-top: 3px; fill: var(--navy); }
  .card-front .band { position: absolute; left: 0; bottom: 0; width: 100%; height: 20px; display: flex; }
  .card-front .band span:nth-child(1) { flex: 0 0 62%; background: linear-gradient(90deg, var(--navy), var(--mid)); }
  .card-front .band span:nth-child(2) { flex: 1; background: var(--navy); }

  /* mailing label + notebook */
  .mail-label { left: 65px; top: 240px; width: 405px; height: 232px; }
  .mail-label .top-bar { position: absolute; left: 0; top: 0; width: 100%; height: 8px; background: var(--navy); }
  .mail-label .wordmark { position: absolute; right: 22px; top: 34px; font-size: 10px; color: var(--navy); }
  .mail-label .return { position: absolute; left: 18px; top: 26px; font-size: 8px; line-height: 1.5; color: var(--navy); }

  .notebook { left: 630px; top: 85px; width: 520px; height: 715px; border-radius: 14px; }
  .notebook .wordmark { position: absolute; left: 0; right: 0; top: 150px; font-size: 21px; }
  .notebook .sub-rule { position: absolute; left: 150px; right: 150px; top: 186px; height: 1px; background: rgba(255,255,255,.6); }
  .binding { position: absolute; left: -14px; top: 30px; display: flex; flex-direction: column; gap: 19.5px; }
  .binding span { display: block; width: 34px; height: 14px; border: 3px solid #c9ccd2; border-radius: 7px; background: transparent; }
</style>
</head>
<body>

<section class="section suite" aria-label="Stationery suite">
  <div class="item paper envelope"><div class="flap"></div></div>

  <div class="item deep mini-back">
    <div class="wordmark center"><span class="mark" style="width:7px;height:7px"></span>Ridgeline Property Group</div>
  </div>
  <div class="item paper mini-front">
    <div class="details"><b>Daniel Harper</b><br>Manager<br>18 Harbor Lane, Suite 310<br>Easton, MA 02375<br>555-014-2200</div>
    <div class="wordmark"><span class="mark" style="width:5px;height:5px"></span>Ridgeline</div>
    <div class="band"></div>
  </div>

  <div class="item paper label-sheet">
    <div class="wordmark"><span class="mark" style="width:10px;height:10px"></span>Ridgeline Property Group</div>
    <div class="return">A Ridgeline Property Group office<br>18 Harbor Lane, Suite 310 Easton, MA 02375</div>
    <div class="band-split"><span></span><span></span><span></span></div>
  </div>

  <div class="item deep folder">
    <div class="wordmark"><span class="mark" style="width:9px;height:9px"></span>Ridgeline Property Group</div>
    <div class="stripe"></div>
  </div>

  <div class="item paper letterhead">
    <div class="edge-top"></div>
    <div class="wordmark"><span class="mark" style="width:8px;height:8px"></span>Ridgeline Property Group</div>
    <div class="rule"></div>
    <div class="footer"><span>18 Harbor Lane, Suite 310, Easton, MA</span><span>555-014-2200</span><span>info@ridgelinepg.com</span></div>
    <div class="edge"></div>
  </div>
</section>

<section class="section cards-showcase" aria-label="Business cards">
  <div class="item deep card-back">
    <div class="wordmark center"><span class="mark" style="width:16px;height:16px"></span>Ridgeline Property Group</div>
    <div class="sub-rule"></div>
  </div>

  <div class="item paper card-front">
    <div class="name">Daniel Harper</div>
    <div class="role">Manager</div>
    <ul class="contact">
      <li><svg width="10" height="12" viewBox="0 0 10 12"><path d="M5 0a4 4 0 0 0-4 4c0 3 4 8 4 8s4-5 4-8a4 4 0 0 0-4-4zm0 5.6A1.6 1.6 0 1 1 5 2.4a1.6 1.6 0 0 1 0 3.2z"/></svg><span>18 Harbor Lane, Suite 310<br>Easton, MA 02375</span></li>
      <li><svg width="10" height="10" viewBox="0 0 10 10"><path d="M2 0l2 2.5-1.2 1.4a6 6 0 0 0 3.3 3.3L7.5 6 10 8l-1.3 2C4 10 0 6 0 1.3z"/></svg><span>555-014-2200</span></li>
      <li><svg width="10" height="10" viewBox="0 0 10 10"><path d="M1 3h8v6H1zM2.5 0h5v2.5h-5z"/></svg><span>555-014-2201</span></li>
      <li><svg width="10" height="10" viewBox="0 0 10 10"><path d="M0 2h10v6H0zM0 2l5 3.5L10 2" stroke="#fff" stroke-width=".8"/></svg><span>info@ridgelinepg.com</span></li>
      <li><svg width="10" height="10" viewBox="0 0 10 10"><circle cx="5" cy="5" r="4.5"/></svg><span>www.ridgelinepg.com</span></li>
    </ul>
    <div class="wordmark"><span class="mark" style="width:11px;height:11px"></span>Ridgeline Property Group</div>
    <div class="band"><span></span><span></span></div>
  </div>
</section>

<section class="section mailing" aria-label="Mailing label and notebook">
  <div class="backdrop"></div>

  <div class="item paper mail-label">
    <div class="top-bar"></div>
    <div class="return">18 Harbor Lane, Suite 310<br>Easton, MA 02375</div>
    <div class="wordmark"><span class="mark" style="width:9px;height:9px"></span>Ridgeline Property Group</div>
    <div class="band-split"><span></span><span></span><span></span></div>
  </div>

  <div class="item deep notebook">
    <div class="binding">
      <span></span><span></span><span></span><span></span><span></span><span></span><span></span><span></span>
      <span></span><span></span><span></span><span></span><span></span><span></span><span></span><span></span>
      <span></span><span></span><span></span><span></span>
    </div>
    <div class="wordmark center"><span class="mark" style="width:15px;height:15px"></span>Ridgeline Property Group</div>
    <div class="sub-rule"></div>
  </div>
</section>

</body>
</html>
```